Verpackungsdesign einer Wassermatte in Baby-Blau gesucht
Zielgruppe
Wir verkaufen Kinder und Baby Produkte. Unsere Zielgruppe sind Eltern und deren Kinder.
Aufgabenstellung
- kindlich
- spielerisch
- mit Logo
- nicht zu bunt
- Hintergrundfarbe von der Verpackung Babyblau
- Maße der Verpackung sind anbei
- Das Produkt ist eine Wassermatte (Fotos anbei)

```html
<!DOCTYPE html>
<html lang="de">
<head>
<meta charset="utf-8">
<title>Kumalu – Baby Wassermatte Faltschachtel</title>
<link rel="stylesheet" href="https://fonts.googleapis.com/css2?family=Abril+Fatface&family=Playfair+Display:wght@900&family=Quicksand:wght@500&family=Source+Sans+3:wght@700&display=swap">
<style>
  :root {
    --paper: #ffffff;
    --baby-blue: #a8dce4;
    --fold-line: #86b7bf;
    --navy: #27306b;
    --water-light: #6fb8dc;
    --water-deep: #1f74b4;
    --bubble: #ffffff;
    --bath-skin: #f0d2b6;
    --bath-tub: #d6ecf2;
  }
  html, body {
    margin: 0;
    padding: 0;
    width: 1200px;
    height: 840px;
    overflow: hidden;
    background: var(--paper);
  }
  .dieline {
    position: relative;
    width: 1200px;
    height: 840px;
  }
  .dieline svg { position: absolute; inset: 0; }
  .panel { fill: var(--baby-blue); }
  .fold { stroke: var(--fold-line); stroke-width: 0.8; fill: none; }
  .bubble { fill: none; stroke: var(--bubble); stroke-width: 2.4; }
  .front-title {
    font-family: "Abril Fatface", "Playfair Display", serif;
    font-size: 42px;
  }
  .front-title .light { fill: var(--paper); }
  .front-title .dark { fill: var(--navy); }
  .brand-name {
    font-family: "Quicksand", sans-serif;
    font-weight: 500;
    fill: var(--navy);
  }
  .brand-dot { fill: var(--navy); }
  .back-heading {
    font-family: "Playfair Display", serif;
    font-weight: 900;
    font-size: 18px;
    fill: var(--navy);
  }
  .back-copy {
    position: absolute;
    top: 348px;
    width: 128px;
    font-family: "Source Sans 3", sans-serif;
    font-weight: 700;
    font-size: 5.3px;
    line-height: 7.3px;
    color: var(--paper);
    text-align: justify;
  }
  .back-copy p { margin: 0 0 7px; }
  .back-copy.col-left { left: 752px; }
  .back-copy.col-right { left: 886px; }
</style>
</head>
<body>
<div class="dieline">
  <svg width="1200" height="840" viewBox="0 0 1200 840" xmlns="http://www.w3.org/2000/svg">
    <defs>
      <linearGradient id="water" x1="0" y1="0" x2="0" y2="1">
        <stop offset="0" stop-color="var(--water-light)"/>
        <stop offset="1" stop-color="var(--water-deep)"/>
      </linearGradient>
      <linearGradient id="bath" x1="0" y1="0" x2="0" y2="1">
        <stop offset="0" stop-color="var(--bath-skin)"/>
        <stop offset="1" stop-color="var(--bath-tub)"/>
      </linearGradient>
      <clipPath id="body-clip">
        <rect x="78" y="244" width="994" height="352"/>
        <path d="M1072 244 L1112 250 V596 H1072 Z"/>
      </clipPath>
    </defs>

    <!-- top closing flap -->
    <path class="panel" d="M192 244 V100 Q192 82 210 82 H556 Q574 82 574 100 V244 Z"/>
    <line class="fold" x1="192" y1="128" x2="574" y2="128"/>
    <!-- dust flaps above side panels -->
    <path class="panel" d="M78 244 V216 L86 156 H182 L192 216 V244 Z"/>
    <path class="panel" d="M574 244 V216 L584 156 H680 L690 216 V244 Z"/>
    <!-- tuck tab above back -->
    <path class="panel" d="M836 294 V222 Q836 192 866 192 H896 Q926 192 926 222 V294 Z"/>
    <line class="fold" x1="836" y1="294" x2="926" y2="294"/>

    <!-- main body panels -->
    <rect class="panel" x="78" y="244" width="994" height="352"/>
    <path class="panel" d="M1072 244 L1112 250 V596 H1072 Z"/>

    <!-- bottom flaps -->
    <path class="panel" d="M78 596 H192 V685 H86 V620 Z"/>
    <path class="panel" d="M338 596 H428 V630 Q428 648 410 648 H356 Q338 648 338 630 Z"/>
    <path class="panel" d="M574 596 H690 V685 H584 V620 Z"/>
    <path class="panel" d="M690 596 H1072 V740 Q1072 758 1054 758 H708 Q690 758 690 740 Z"/>
    <line class="fold" x1="690" y1="712" x2="1072" y2="712"/>

    <!-- water band -->
    <path clip-path="url(#body-clip)" fill="url(#water)" d="M78 494 Q150 478 230 490 T400 486 T560 492 T720 484 T880 490 T1040 482 L1112 488 V596 H78 Z"/>

    <!-- fold lines -->
    <g class="fold">
      <line x1="78" y1="244" x2="1112" y2="244"/>
      <line x1="78" y1="596" x2="1112" y2="596"/>
      <line x1="192" y1="156" x2="192" y2="685"/>
      <line x1="574" y1="156" x2="574" y2="685"/>
      <line x1="690" y1="156" x2="690" y2="758"/>
      <line x1="1072" y1="244" x2="1072" y2="596"/>
    </g>

    <!-- bubbles -->
    <g class="bubble">
      <circle cx="236" cy="250" r="24"/>
      <circle cx="115" cy="292" r="24"/>
      <circle cx="136" cy="446" r="18"/>
      <circle cx="151" cy="537" r="24"/>
      <circle cx="274" cy="527" r="10"/>
      <circle cx="467" cy="380" r="24"/>
      <circle cx="526" cy="219" r="11"/>
      <circle cx="221" cy="326" r="10"/>
      <circle cx="263" cy="306" r="8"/>
      <circle cx="529" cy="298" r="8"/>
      <circle cx="478" cy="196" r="8"/>
      <circle cx="124" cy="626" r="8"/>
      <circle cx="703" cy="284" r="24"/>
      <circle cx="730" cy="341" r="8"/>
      <circle cx="651" cy="482" r="18"/>
      <circle cx="663" cy="552" r="29"/>
      <circle cx="1063" cy="301" r="24"/>
      <circle cx="1064" cy="402" r="18"/>
      <circle cx="1052" cy="518" r="8"/>
      <circle cx="1053" cy="584" r="29"/>
    </g>

    <!-- front: brand -->
    <circle class="brand-dot" cx="332" cy="297" r="14"/>
    <text class="brand-name" x="354" y="305" font-size="22">Kumalu</text>

    <!-- front: product title -->
    <g class="front-title" transform="translate(236 418) rotate(-20)">
      <text class="light" x="0" y="0">Baby</text>
      <text class="dark" x="-8" y="46">Wasser-</text>
      <text class="dark" x="22" y="92">matte</text>
    </g>

    <!-- front: bath illustration area -->
    <rect x="420" y="412" width="184" height="184" rx="44" fill="url(#bath)"
          role="img" aria-label="Illustration eines Babys in einer kleinen Badewanne"/>

    <!-- back: heading -->
    <text class="back-heading" x="882" y="325" text-anchor="middle">Baby Wassermatte</text>
    <rect x="802" y="333" width="154" height="2.4" fill="var(--navy)"/>

    <!-- back: brand -->
    <circle class="brand-dot" cx="843" cy="553" r="14"/>
    <text class="brand-name" x="862" y="561" font-size="20">Kumalu</text>
  </svg>

  <div class="back-copy col-left">
    <p>Die weiche Wassermatte lädt kleine Hände zum Entdecken ein. Bunte Formen schwimmen unter der Oberfläche und bewegen sich bei jeder Berührung sanft hin und her.</p>
    <p>Ideal für die Bauchlage: Ihr Baby stärkt Nacken, Rücken und Arme, während es spielerisch die Welt erkundet.</p>
    <p>Einfach mit Wasser füllen, Ventil schließen und loslegen. Die robuste Folie ist frei von Schadstoffen und lässt sich leicht reinigen.</p>
    <p>Auch für unterwegs: Die Matte ist leicht, faltbar und passt in jede Tasche. So bleibt Ihr Kind überall gut beschäftigt und zufrieden.</p>
  </div>
  <div class="back-copy col-right">
    <p>Geeignet ab drei Monaten. Nur unter Aufsicht eines Erwachsenen verwenden. Nicht auf spitze oder heiße Flächen legen und vor direkter Sonne schützen.</p>
    <p>Füllmenge: etwa ein Liter lauwarmes Wasser. Nach dem Spielen vollständig entleeren und trocknen lassen, bevor die Matte verstaut wird.</p>
    <p>Inhalt: eine Wassermatte, ein Reparaturset. Maße gefüllt ca. 66 x 50 cm. Material: PVC, frei von BPA und Phthalaten.</p>
    <p>Bitte Verpackung für spätere Rückfragen aufbewahren. Wir wünschen viel Freude beim gemeinsamen Spielen und Entdecken.</p>
  </div>
</div>
</body>
</html>
```